HARLOWE CONSERVATORY SAXOPHONE SENIOR RECITAL

I need a poster design for my senior saxophone recital. The title of it is "Quill: a Voyage beneath the Edge of Tone". My concept is completely contrasting to the idea of a typical university recital. I'm so put off by the idea of "clap..clap..{play some music}..clap..clap..repeat". My recital is all based off of sound. The music I selected is all very modern (i.e Brem Ostrakel 'Warm from the First Pour' for Saxophone and Coffee Machine). I've included the Chatterbox link so you can see the picture I have in the background. I like the idea of minimal black and white photography. Also, I would like the time / date / location / etc. all included on it. Let your imaginations run wild! It's art for an artist!
https://www.chatterbox-example.net/events/412093857716230/
Target Market(s)
University Students around the Harlowe Conservatory and locals around the art district of South Beach, FL.
Industry/Entity Type
University
Look and feel

```html
<!DOCTYPE html>
<html lang="en">
<head>
<meta charset="utf-8">
<title>Quill: a Voyage beneath the Edge of Tone</title>
<link href="https://fonts.googleapis.com/css2?family=Jost:wght@200;300;500;700&display=swap" rel="stylesheet">
<style>
  :root {
    --paper: #fbfbfb;
    --ink: #0b0b0b;
    --tone-mid: #3c3c3c;
    --light-text: #f2f2f2;
    --sky: #d4d4d4;
    --ridge: #4e4e4e;
    --water-light: #dadada;
    --water-dark: #2a2a2a;
    --deep: #111111;
  }
  html, body {
    margin: 0;
    padding: 0;
    overflow: hidden;
    background: var(--paper);
  }
  .poster {
    position: relative;
    width: 849px;
    height: 1200px;
    background: var(--paper);
    overflow: hidden;
    font-family: "Jost", "Futura", sans-serif;
  }
  .lake-photo {
    position: absolute;
    left: 12px;
    top: 12px;
    width: 825px;
    height: 1176px;
    border-radius: 6px;
    background:
      radial-gradient(ellipse 75% 60% at 50% 52%, rgba(255,255,255,0) 55%, rgba(0,0,0,0.5) 100%),
      linear-gradient(to bottom,
        #bdbdbd 0%,
        var(--sky) 12%,
        #e4e4e4 20%,
        #9a9a9a 26%,
        #6a6a6a 32%,
        var(--water-light) 35.5%,
        #a8a8a8 38%,
        #8a8a8a 41%,
        #b6b6b6 45%,
        var(--water-light) 52%,
        #d0d0d0 60%,
        #9a9a9a 70%,
        #555555 82%,
        var(--water-dark) 91%,
        var(--deep) 100%);
  }
  .title {
    position: absolute;
    top: 128px;
    left: 0;
    width: 849px;
    margin: 0;
    text-align: center;
    font-weight: 700;
    font-size: 134px;
    line-height: 1;
    letter-spacing: 0.2em;
    padding-left: 0.2em;
    box-sizing: border-box;
    color: var(--ink);
  }
  .subtitle {
    position: absolute;
    top: 282px;
    left: 16px;
    width: 849px;
    margin: 0;
    text-align: center;
    font-size: 64px;
    line-height: 75px;
    font-weight: 200;
    color: var(--ink);
    letter-spacing: -0.01em;
  }
  .subtitle span { display: block; }
  .subtitle .emphasis { font-weight: 500; }
  .subtitle .fade { font-weight: 300; color: var(--tone-mid); }
  .recital-credit,
  .recital-details {
    position: absolute;
    left: 16px;
    width: 849px;
    margin: 0;
    text-align: center;
    font-size: 11px;
    font-weight: 500;
    letter-spacing: 0.22em;
    color: var(--light-text);
  }
  .recital-credit { top: 978px; }
  .recital-details { top: 1000px; font-weight: 300; }
</style>
</head>
<body>
  <main class="poster">
    <div class="lake-photo" role="img" aria-label="Black and white photograph of a person seen from behind, sitting at the bow of a boat on a still mountain lake with misty peaks reflected in the water"></div>
    <h1 class="title">QUILL</h1>
    <h2 class="subtitle">
      <span>A VOYAGE</span>
      <span>BENEATH THE</span>
      <span class="emphasis">EDGE OF</span>
      <span class="fade">TONE</span>
    </h2>
    <p class="recital-credit">DARIO VENTURELLI SENIOR SAXOPHONE RECITAL</p>
    <p class="recital-details">FRIDAY, APRIL 18 · 7:30 PM · LYRA HALL, HARLOWE CONSERVATORY</p>
  </main>
</body>
</html>
```